Stationery Design For Specialist London law firm

We have merged two firms of London lawyers to create a new firm with a new name.

The new firms name is KR Holloway. We would like to include the description Solicitors and Advocates in the design.

We need a new design for our headed paper, business cards compliment slips etc.

The image we wish to project is fresh but not gimmicky - reliable and strong but not stuffy.

We have no strong views on font or colour this really is pretty much a blank page.

Our preference is for the name to be at the top of the page

Target Market(s)

Our clients who are individuals rather than corporate and other lawyers

Industry/Entity Type

Law Firm

Requirements
Should not have
• Legal images eg scales of justice etc

Obviously nothing childish or gimmicky

```html
<!DOCTYPE html>
<html lang="en">
<head>
<meta charset="utf-8">
<title>KR Holloway – Business Card</title>
<link href="https://fonts.googleapis.com/css2?family=Tinos:wght@400;700&family=Arimo:wght@400&display=swap" rel="stylesheet">
<style>
  :root {
    --backdrop: #4a4a4a;
    --card-dark: #000000;
    --card-light: #f1f1f1;
    --brand-blue: #1f6dbd;
    --rule-blue: #3b66a3;
    --ink: #111111;
    --ink-light: #ffffff;
    --divider-dark: #8a8a8a;
    --divider-light: #9a9a9a;
  }
  * { margin: 0; padding: 0; box-sizing: border-box; }
  html, body { width: 1200px; height: 900px; overflow: hidden; }
  body {
    position: relative;
    background: var(--backdrop);
    font-family: "Arimo", Arial, sans-serif;
  }
  .card {
    position: absolute;
    top: 300px;
    width: 525px;
    height: 300px;
    border-radius: 22px;
    overflow: hidden;
  }
  .card--front { left: 58px; background: var(--card-dark); }
  .card--back { left: 617px; background: var(--card-light); }
  .card > * { position: absolute; }

  .brand-square { background: var(--brand-blue); }
  .brand-divider { width: 1px; }
  .brand-name {
    font-family: "Tinos", "Times New Roman", serif;
    font-weight: 700;
    color: var(--brand-blue);
    line-height: 1;
    white-space: nowrap;
  }
  .brand-tagline {
    font-family: "Tinos", "Times New Roman", serif;
    font-weight: 400;
    line-height: 1;
    white-space: nowrap;
  }

  /* front */
  .card--front .brand-square { left: 79px; top: 105px; width: 82px; height: 89px; }
  .card--front .brand-divider { left: 177px; top: 115px; height: 70px; background: var(--divider-dark); }
  .card--front .brand-name { left: 192px; top: 119px; font-size: 46px; }
  .card--front .brand-tagline { left: 193px; top: 161px; font-size: 22px; color: var(--ink-light); }

  .web-rule { height: 2px; background: var(--rule-blue); left: 0; }
  .card--front .web-rule { top: 265px; width: 324px; }
  .web-address {
    font-size: 14px;
    letter-spacing: 1.6px;
    line-height: 1;
    white-space: nowrap;
  }
  .card--front .web-address { left: 332px; top: 259px; color: var(--ink-light); }

  /* back */
  .card--back .brand-square { left: 52px; top: 59px; width: 52px; height: 57px; }
  .card--back .brand-divider { left: 115px; top: 66px; height: 43px; background: var(--divider-light); }
  .card--back .brand-name { left: 124px; top: 68px; font-size: 30px; }
  .card--back .brand-tagline { left: 124px; top: 94px; font-size: 14.5px; color: var(--ink); }

  .contact { left: 52px; top: 166px; color: var(--ink); line-height: 1; }
  .contact-address { font-size: 13.5px; margin-bottom: 8px; }
  .contact-row { font-size: 12px; margin-bottom: 4px; white-space: nowrap; }
  .contact-row .item { margin-right: 6px; }
  .contact-label { color: var(--brand-blue); }

  .person { right: 27px; top: 167px; text-align: right; line-height: 1; }
  .person-name { font-size: 18px; color: var(--brand-blue); }
  .person-role { font-size: 11.5px; color: var(--ink); margin-top: 3px; }

  .edge-tab {
    right: 0; top: 165px; width: 13px; height: 33px;
    background: var(--card-dark); border-radius: 4px 0 0 4px;
  }
  .card--back .web-rule { top: 266px; width: 323px; }
  .card--back .web-address { left: 331px; top: 260px; color: var(--ink); }
</style>
</head>
<body>
  <section class="card card--front" aria-label="Business card front">
    <div class="brand-square"></div>
    <div class="brand-divider"></div>
    <div class="brand-name">KR Holloway</div>
    <div class="brand-tagline">Solicitors and Advocates</div>
    <div class="web-rule"></div>
    <div class="web-address">www.krholloway.com</div>
  </section>

  <section class="card card--back" aria-label="Business card back">
    <div class="brand-square"></div>
    <div class="brand-divider"></div>
    <div class="brand-name">KR Holloway</div>
    <div class="brand-tagline">Solicitors and Advocates</div>

    <div class="contact">
      <p class="contact-address">00000 KR Holloway, Your Adress 00000</p>
      <p class="contact-row"><span class="item"><span class="contact-label">p:</span> 123-400-5511</span> <span class="item"><span class="contact-label">m:</span> 123-600-5511</span></p>
      <p class="contact-row"><span class="item"><span class="contact-label">f:</span> 123-700-5511</span> <span class="item"><span class="contact-label">e:</span> email@krholloway.com</span></p>
    </div>

    <div class="person">
      <p class="person-name">Marian Castell</p>
      <p class="person-role">Owner</p>
    </div>

    <div class="edge-tab"></div>
    <div class="web-rule"></div>
    <div class="web-address">www.krholloway.com</div>
  </section>
</body>
</html>
```